Letterhead and Envelopes design using existing logo. Logo can be found at tqvanholt.com

Use existing logo (attached) and incorporate in letterhead and envelope designs.

Current logo can be viewed at tqvanholt.com the web site reflect various parent and sub companies. Please see attached as well.

Target Market(s)

Other oil and gas operators.

Industry/Entity Type

Oil And Gas

Font styles to use
Sans Serif

Colors

Designer to choose colors to be used in the design.

Requirements
Must have
• Current logo and address
Nice to have
• Modern, contemporary approach yet incorporate existing traditional design.
• After design is selected for Wexford Tiller Holdings I will use similar design for Royalties, Exploration, Energy and Farms with different color schemes.

```html
<!DOCTYPE html>
<html lang="en">
<head>
<meta charset="utf-8">
<title>Wexford Tiller Holdings — Letterhead</title>
<link href="https://fonts.googleapis.com/css2?family=Roboto:wght@400;500&family=Montserrat:wght@400&display=swap" rel="stylesheet">
<style>
  :root {
    --backdrop: #e4e4e4;
    --paper: #f1f1f1;
    --ink: #7a7a7a;
    --ink-dark: #3a3a3a;
    --brand-green: #5a8f2a;
    --mark-black: #111111;
  }
  * { margin: 0; padding: 0; box-sizing: border-box; }
  html, body {
    width: 1200px; height: 866px; overflow: hidden;
    background: var(--backdrop);
  }
  .letterhead {
    position: absolute; left: 333px; top: 58px;
    width: 534px; height: 749px;
    background: var(--paper);
    font-family: 'Roboto', Arial, sans-serif;
    color: var(--ink);
  }
  .brand {
    position: absolute; left: 46px; top: 50px;
    display: flex; align-items: center; gap: 12px;
  }
  .brand-dot {
    width: 22px; height: 22px; border-radius: 50%;
    background: var(--brand-green);
  }
  .brand-name {
    font-weight: 500; font-size: 17px; color: var(--ink-dark);
    letter-spacing: 0.02em; text-transform: uppercase; line-height: 1.2;
    width: 150px;
  }
  .recipient {
    position: absolute; left: 46px; top: 228px;
    font-size: 10px; line-height: 14px;
  }
  .body-copy {
    position: absolute; left: 46px; width: 444px;
    font-size: 9.6px; line-height: 14px; text-align: justify;
  }
  .body-copy.first { top: 311px; }
  .body-copy.second { top: 436px; }
  .signature {
    position: absolute; left: 46px; top: 510px;
    width: 104px; height: 68px;
  }
  .sign-title {
    position: absolute; left: 46px; top: 652px;
    font-size: 10px;
  }
  .contact-bar {
    position: absolute; left: 50px; top: 690px;
    display: flex; align-items: center;
    font-family: 'Montserrat', Arial, sans-serif;
    font-size: 9.6px; line-height: 11px; color: var(--ink-dark);
  }
  .contact-item { display: flex; align-items: center; gap: 8px; }
  .contact-icon { width: 20px; height: 20px; flex: none; }
  .contact-divider {
    width: 2px; height: 24px; background: var(--brand-green);
    margin: 0 24px;
  }
</style>
</head>
<body>
  <main class="letterhead">
    <header class="brand">
      <span class="brand-dot"></span>
      <span class="brand-name">Wexford Tiller Holdings</span>
    </header>

    <address class="recipient" style="font-style:normal">
      Dear Halvorsen<br>
      Corlin Print Partners<br>
      Department Design
    </address>

    <p class="body-copy first">Lorem ipsum dolor sit amet, consectetuer adipiscing elit. Aenean commodo ligula eget dolor. Aenean massa. Cum sociis natoque penatibus et magnis dis parturient montes, nascetur ridiculus mus. Donec quam felis, ultricies nec, pellentesque eu, pretium quis, sem. Nulla consequat massa quis enim. Donec pede justo, fringilla vel, aliquet nec, vulputate eget, arcu. In enim justo, rhoncus ut, imperdiet a, venenatis vitae, justo. Nullam dictum felis eu pede mollis pretium. Integer tincidunt. Cras dapibus. Vivamus elementum semper nisi.Nullam dictum felis eu pede mollis pretium. Integer tincidunt. Cras dapibus. Vivamus elementum semper nisi.felis eu pede mollis pretium. Integer tincidunt. Cras dapibus.</p>

    <p class="body-copy second">Quisque rutrum. Aenean imperdiet. Etiam ultricies nisi vel augue. Curabitur ullamcorper ultricies nisi. Nam eget dui. Etiam rhoncus. Maecenas tempus, tellus eget condimentum rhoncus, sem quam semper libero, sit amet adipiscing sem neque sed ipsum.felis pede mollis pretium. I am tincidunt. Cras dapibus.</p>

    <div class="signature" role="img" aria-label="Handwritten signature of the director" style="background: linear-gradient(135deg, rgba(90,143,42,0.18), rgba(90,143,42,0.06));"></div>

    <p class="sign-title">Director/Excecutive Director</p>

    <footer class="contact-bar">
      <div class="contact-item">
        <svg class="contact-icon" viewBox="0 0 20 20" aria-hidden="true">
          <circle cx="10" cy="10" r="10" fill="var(--brand-green)"/>
          <path d="M6.5 5.5 l2 -0.3 1 2.4 -1.2 1 a7 7 0 0 0 3 3 l1 -1.2 2.4 1 -0.3 2 c-4.5 0.4 -8.3 -3.4 -7.9 -7.9z" fill="#fff"/>
        </svg>
        <span>701-555-0148<br>701-555-0148</span>
      </div>
      <span class="contact-divider"></span>
      <div class="contact-item">
        <svg class="contact-icon" viewBox="0 0 20 20" aria-hidden="true">
          <circle cx="10" cy="10" r="10" fill="var(--brand-green)"/>
          <rect x="5" y="6.5" width="10" height="7" rx="1" fill="#fff"/>
          <path d="M5.3 7 L10 10.6 14.7 7" fill="none" stroke="var(--brand-green)" stroke-width="1"/>
        </svg>
        <span>info@tqvanholt.com<br>www.tqvanholt.com</span>
      </div>
      <span class="contact-divider"></span>
      <div class="contact-item">
        <svg class="contact-icon" viewBox="0 0 20 20" aria-hidden="true">
          <circle cx="10" cy="10" r="10" fill="var(--brand-green)"/>
          <circle cx="10" cy="10" r="5.5" fill="none" stroke="#fff" stroke-width="1.2"/>
          <path d="M4.5 10 h11 M10 4.5 c-2.5 3 -2.5 8 0 11 M10 4.5 c2.5 3 2.5 8 0 11" fill="none" stroke="#fff" stroke-width="1"/>
        </svg>
        <span>PO Box 418 Harlow<br>North Dakota 58990</span>
      </div>
    </footer>
  </main>
</body>
</html>
```